Minimalistic logo and website for plovrak.com

My colleague and I just started a new company. We need a website to replace the placeholder at https://plovrak.com/

We need a onepager website. A logotype and color profiles. We like minimalism. Scandinavian design.

Below is just information about the company. You can rearrange it, add photos, emit stuff. Maybe even add stuff if you think it is necessary.

# About Plovrak
Plovrak builds critical applications to capture new markets, create modern services and captivate our customers in new and engaging ways. Creating effective and engaging solutions that truly work has always been Plovrak's core offering and is what makes us excited to work in digital. We are a forward thinking company embracing the opportunities of digital transformation and automations.

# Core services
Business automation
Application development and services for desktop and mobile
Interface Design and UX
Enterprise integrations

# Some more data
Plovrak was founded by Torvald Bergqvist and Mikael Dahlgren in 2021.
NetLinkPro: https://www.netlinkpro.example/company/74819203/admin/

# Inspiration
Minimal. Simple.
https://www.brunvikformstudio.se/contact

Target Market(s)

Businesses

Industry/Entity Type

IT, business automation, data

Number of Pages Required

1 page

Font styles to use
Sans Serif

Colors

Designer to choose colors to be used in the design.

Requirements
Must have
• Onepage design. Minimalism.
Should not have
• Menus

```html
<!DOCTYPE html>
<html lang="en">
<head>
<meta charset="utf-8">
<title>Plovrak — Digital transformation and automation</title>
<link rel="stylesheet" href="https://fonts.googleapis.com/css2?family=Montserrat:wght@400;500;600;700&display=swap">
<style>
  :root {
    --ink: #111111;
    --text: #2a2a2a;
    --muted: #6b6b6b;
    --white: #ffffff;
    --soft: #f8f6f7;
    --footer: #050505;
    --hero-a: #0b1f3a;
    --hero-b: #2a4f7d;
    --hero-c: #7fa3c7;
  }
  * { box-sizing: border-box; margin: 0; padding: 0; }
  html, body { width: 1200px; height: 2928px; overflow: hidden; }
  body { font-family: "Montserrat", Arial, sans-serif; color: var(--text); background: var(--white); }
  .wrap { width: 984px; margin: 0 auto; }

  .site-header { height: 90px; display: flex; align-items: center; }
  .site-header .wrap { display: flex; justify-content: space-between; align-items: center; }
  .brand { font-weight: 700; font-size: 30px; color: var(--ink); letter-spacing: -0.5px; }
  .menu-toggle { width: 28px; height: 20px; }

  .hero { position: relative; height: 640px; overflow: hidden;
    background: linear-gradient(115deg, var(--hero-a) 0%, #1a365c 45%, var(--hero-b) 70%, var(--hero-c) 100%); }
  .hero-photo { position: absolute; inset: 0;
    background: radial-gradient(ellipse at 78% 55%, rgba(170,205,240,0.45), transparent 55%), linear-gradient(90deg, rgba(5,15,35,0.55), rgba(5,15,35,0.1)); }
  .hero .wrap { position: relative; padding-top: 140px; }
  .hero h1 { font-size: 58px; font-weight: 700; color: var(--white); letter-spacing: 1px; }
  .hero p { margin-top: 24px; width: 470px; font-size: 22px; line-height: 30px; color: var(--white); font-weight: 500; }
  .btn { display: inline-block; margin-top: 52px; background: var(--white); color: var(--ink);
    font-size: 13px; font-weight: 600; padding: 20px 20px; letter-spacing: 0.3px; text-decoration: none; }

  .about { height: 315px; padding-top: 80px; }
  .about .wrap { display: flex; justify-content: space-between; }
  .eyebrow { font-size: 12px; font-weight: 500; letter-spacing: 1px; color: var(--ink); text-transform: uppercase; }
  .about h2 { margin-top: 14px; font-size: 42px; line-height: 46px; font-weight: 700; color: var(--ink); }
  .about p { width: 500px; font-size: 14px; line-height: 26px; color: var(--muted); }

  .services { background: var(--soft); height: 1115px; padding-top: 68px; text-align: center; }
  .section-title { margin-top: 16px; font-size: 44px; font-weight: 700; color: var(--ink); letter-spacing: 0.5px; }
  .service-grid { margin-top: 60px; display: grid; grid-template-columns: 472px 472px; column-gap: 40px; row-gap: 36px; text-align: left; }
  .service-img { height: 322px; }
  .service h3 { margin-top: 20px; font-size: 19px; line-height: 26px; font-weight: 600; color: var(--ink); width: 360px; }

  .news { height: 585px; padding-top: 66px; text-align: center; }
  .news-grid { margin-top: 50px; display: grid; grid-template-columns: repeat(3, 1fr); column-gap: 22px; text-align: left; }
  .news-img { height: 220px; }
  .news-date { margin-top: 18px; font-size: 13px; color: var(--muted); display: flex; align-items: center; gap: 6px; }
  .news h3 { margin-top: 8px; font-size: 18px; line-height: 24px; font-weight: 600; color: var(--ink); }

  .site-footer { background: var(--footer); color: var(--white); height: 183px; padding-top: 40px; }
  .site-footer .wrap { display: flex; }
  .footer-brand .brand { color: var(--white); font-size: 34px; }
  .footer-brand small { display: block; margin-top: 18px; font-size: 11px; color: #cccccc; }
  .footer-col { font-size: 11px; line-height: 17px; color: #dddddd; }
  .footer-col h4 { font-size: 15px; font-weight: 600; color: var(--white); margin-bottom: 8px; }
  .col-1 { width: 297px; } .col-2 { width: 235px; } .col-3 { width: 292px; }
  .social { display: flex; align-items: center; gap: 6px; }
  .social i { width: 10px; height: 10px; background: var(--white); display: inline-block; }
</style>
</head>
<body>
  <header class="site-header">
    <div class="wrap">
      <div class="brand">Plovrak.</div>
      <svg class="menu-toggle" viewBox="0 0 28 20" aria-label="Menu toggle"><rect x="0" y="2" width="28" height="2" fill="#111"/><rect x="8" y="9" width="20" height="2" fill="#111"/><rect x="0" y="16" width="28" height="2" fill="#111"/></svg>
    </div>
  </header>

  <section class="hero">
    <div class="hero-photo" role="img" aria-label="Person in a suit touching a glowing network of connected data points"></div>
    <div class="wrap">
      <h1>PLOVRAK</h1>
      <p>We are a forward thinking company embracing the opportunities of digital transformation and automations.</p>
      <a class="btn" href="#about">GET MORE INFO</a>
    </div>
  </section>

  <section class="about" id="about">
    <div class="wrap">
      <div>
        <div class="eyebrow">Welcome</div>
        <h2>ABOUT<br>PLOVRAK</h2>
      </div>
      <p>Plovrak builds critical applications to capture new markets, create modern services and captivate our customers in new and engaging ways. Creating effective and engaging solutions that truly work has always been Plovrak's core offering and is what makes us excited to work in digital. We are a forward thinking company embracing the opportunities of digital transformation and automations.</p>
    </div>
  </section>

  <section class="services">
    <div class="wrap">
      <div class="eyebrow">Services</div>
      <h2 class="section-title">WHAT WE DO</h2>
      <div class="service-grid">
        <div class="service">
          <div class="service-img" role="img" aria-label="Hands typing on a laptop with a glowing light" style="background:linear-gradient(135deg,#d9dde2,#b7a08a 60%,#e8c27a)"></div>
          <h3>Business<br>automation</h3>
        </div>
        <div class="service">
          <div class="service-img" role="img" aria-label="Hands using a tablet beside printed charts" style="background:linear-gradient(135deg,#eef0f2,#c9ccd0 55%,#8a7566)"></div>
          <h3>Application development and services for desktop and mobile</h3>
        </div>
        <div class="service">
          <div class="service-img" role="img" aria-label="Team reviewing interface layouts on tablets and paper" style="background:linear-gradient(135deg,#cfd6dc,#e7e2da 50%,#b58a5e)"></div>
          <h3>Interface<br>Design and UX</h3>
        </div>
        <div class="service">
          <div class="service-img" role="img" aria-label="Hands joining white puzzle pieces on a wooden table" style="background:linear-gradient(135deg,#a06a43,#d8b99a 55%,#f2ece4)"></div>
          <h3>Enterprise<br>integrations</h3>
        </div>
      </div>
    </div>
  </section>

  <section class="news">
    <div class="wrap">
      <div class="eyebrow">Post</div>
      <h2 class="section-title">IN THE NEWS</h2>
      <div class="news-grid">
        <article>
          <div class="news-img" role="img" aria-label="Team stacking hands together in a circle" style="background:linear-gradient(135deg,#9fb6c8,#e4e8ec 55%,#c79a78)"></div>
          <div class="news-date"><svg width="12" height="12" viewBox="0 0 12 12"><rect x="1" y="2" width="10" height="9" fill="none" stroke="#6b6b6b"/><line x1="1" y1="5" x2="11" y2="5" stroke="#6b6b6b"/></svg>11/01/2022</div>
          <h3>Lorem ipsum dolor sit amet, consectetur adipi</h3>
        </article>
        <article>
          <div class="news-img" role="img" aria-label="Colleagues planning with sticky notes on a glass wall" style="background:linear-gradient(135deg,#eef0f3,#c8d3de 50%,#e3b7a0)"></div>
          <div class="news-date"><svg width="12" height="12" viewBox="0 0 12 12"><rect x="1" y="2" width="10" height="9" fill="none" stroke="#6b6b6b"/><line x1="1" y1="5" x2="11" y2="5" stroke="#6b6b6b"/></svg>11/01/2022</div>
          <h3>Lorem ipsum dolor sit amet, consectetur adipi</h3>
        </article>
        <article>
          <div class="news-img" role="img" aria-label="Office worker using a tablet in a bright room" style="background:linear-gradient(135deg,#f1f1f1,#d7cfc6 55%,#a8b4bf)"></div>
          <div class="news-date"><svg width="12" height="12" viewBox="0 0 12 12"><rect x="1" y="2" width="10" height="9" fill="none" stroke="#6b6b6b"/><line x1="1" y1="5" x2="11" y2="5" stroke="#6b6b6b"/></svg>11/01/2022</div>
          <h3>Lorem ipsum dolor sit amet, consectetur adipi</h3>
        </article>
      </div>
    </div>
  </section>

  <footer class="site-footer">
    <div class="wrap">
      <div class="footer-brand col-1">
        <div class="brand">Plovrak.</div>
        <small>Copyright © 2022, Plovrak.</small>
      </div>
      <div class="footer-col col-2">
        <h4>Get directions</h4>
        Headquarters<br>Northvale,<br>Eastmere Bay 7730
      </div>
      <div class="footer-col col-3">
        <h4>Quick Links</h4>
        Privacy policy<br>Subscribe to our newsletter
      </div>
      <div class="footer-col">
        <h4>Social Media</h4>
        <div class="social"><i></i>NetLinkPro</div>
      </div>
    </div>
  </footer>
</body>
</html>
```